SKYTHRESH (drone photo and video) and Photogrammetry Services (mapping and 3D modeling)

We need a business card design for a SKYTHRESH. Our businesses provides (drone) Aerial Photo and Video Captures. However we also provide Photogrammetry (which is 3D modeling and mapping). We greatly value unique points of view taken of landscapes and subjects with aerial photography and videography. 3D modeling and mapping is the other area of focus and have an incredibly broad scope of applications and imaginative creativity.

Target Market(s)

Based out of Northern Virginia and serving the greater Virginia and Maryland areas

Industry/Entity Type

Drone Photo and video and Photogrammetry Services (mapping and 3D modeling)

Contact Information for Business Card

3D Models, Maps and Photo/Video Production name: Marcus Lindqvist email: mrl@skythresh.us website: skythresh.us phone: 571-308-6943; please also include "Aerial Photo/Video and 3D Mapping/Modeling"

Requirements
Must have
• Please make this design vertical and double sided. The selection box is not letting me choose Double Sided but that is my wish. Incorporate uploaded LOGO and color scheme
Nice to have
• Preferably does not feel too crowded and balances not having an exaggerated amount of distracting detail
Should not have
• do not cram bullet points or text in long form

```html
<!DOCTYPE html>
<html lang="en">
<head>
<meta charset="utf-8">
<title>SKYTHRESH Business Card</title>
<link href="https://fonts.googleapis.com/css2?family=Lato:wght@400;700;900&display=swap" rel="stylesheet">
<style>
  :root {
    --bg: #6e6e6e;
    --yellow: #fbb22a;
    --orange: #ff6a24;
    --red: #ff1329;
    --white: #ffffff;
    --ink: #111111;
    --snow: #f1f1f1;
  }
  * { box-sizing: border-box; margin: 0; padding: 0; }
  html, body { width: 1200px; height: 875px; overflow: hidden; }
  body {
    background: var(--bg);
    font-family: "Lato", sans-serif;
    position: relative;
  }
  .card {
    position: absolute;
    border-radius: 22px;
    overflow: hidden;
    box-shadow: 0 18px 40px rgba(0,0,0,0.35);
  }
  .card-front {
    left: 150px; top: 157px;
    width: 320px; height: 560px;
    background: linear-gradient(200deg, var(--red) 0%, var(--orange) 55%, var(--yellow) 100%);
    color: var(--white);
  }
  .contact-block {
    position: absolute;
    top: 56px; left: 16px; right: 16px;
    text-align: center;
  }
  .person-name {
    font-weight: 700;
    font-size: 25px;
    letter-spacing: 1px;
    text-transform: uppercase;
    white-space: nowrap;
  }
  .person-role {
    font-size: 12px;
    margin-top: 5px;
    letter-spacing: 0.2px;
    white-space: nowrap;
  }
  .icon-row {
    display: flex;
    justify-content: center;
    gap: 8px;
    margin-top: 18px;
  }
  .icon-dot {
    width: 24px; height: 24px;
    border-radius: 50%;
    background: var(--white);
    display: flex; align-items: center; justify-content: center;
  }
  .icon-dot svg { width: 14px; height: 14px; }
  .contact-lines {
    margin-top: 18px;
    font-size: 15px;
    line-height: 1.5;
  }
  .scene-art {
    position: absolute;
    left: 0; right: 0; bottom: 0;
    height: 250px;
    background: linear-gradient(180deg, rgba(255,255,255,0) 0%, rgba(255,255,255,0.35) 45%, rgba(241,241,241,0.6) 100%);
  }
  .card-back {
    left: 560px; top: 277px;
    width: 560px; height: 320px;
    background: var(--white);
    display: flex; align-items: center; justify-content: center;
    gap: 18px;
  }
  .brand-dot {
    width: 70px; height: 70px;
    border-radius: 50%;
    background: var(--orange);
  }
  .brand-name {
    font-weight: 900;
    font-size: 52px;
    letter-spacing: 2px;
    color: var(--ink);
  }
</style>
</head>
<body>
  <section class="card card-front">
    <div class="contact-block">
      <h1 class="person-name">Marcus Lindqvist</h1>
      <p class="person-role">Aerial Photo/Video and 3D Mapping/Modeling</p>
      <div class="icon-row">
        <span class="icon-dot">
          <svg viewBox="0 0 24 24" aria-label="phone"><path fill="#ff4a26" d="M6.6 10.8a15 15 0 0 0 6.6 6.6l2.2-2.2a1 1 0 0 1 1-.25 11.4 11.4 0 0 0 3.6.57 1 1 0 0 1 1 1V20a1 1 0 0 1-1 1A17 17 0 0 1 3 4a1 1 0 0 1 1-1h3.5a1 1 0 0 1 1 1c0 1.25.2 2.45.57 3.57a1 1 0 0 1-.25 1z"/></svg>
        </span>
        <span class="icon-dot">
          <svg viewBox="0 0 24 24" aria-label="email"><path fill="#ff4a26" d="M3 5h18a1 1 0 0 1 1 1v12a1 1 0 0 1-1 1H3a1 1 0 0 1-1-1V6a1 1 0 0 1 1-1zm1 2v.5l8 5 8-5V7l-8 5z"/></svg>
        </span>
        <span class="icon-dot">
          <svg viewBox="0 0 24 24" aria-label="website"><path fill="#ff4a26" d="M12 2a7 7 0 0 1 7 7c0 5-7 13-7 13S5 14 5 9a7 7 0 0 1 7-7zm0 4.5A2.5 2.5 0 1 0 12 11.5 2.5 2.5 0 0 0 12 6.5z"/></svg>
        </span>
      </div>
      <div class="contact-lines">
        <p>571-308-6943</p>
        <p>mrl@skythresh.us</p>
        <p>skythresh.us</p>
      </div>
    </div>
    <div class="scene-art" role="img" aria-label="Illustration of white snowy mountain peaks with a drone flying beside them"></div>
  </section>

  <section class="card card-back">
    <span class="brand-dot"></span>
    <span class="brand-name">SKYTHRESH</span>
  </section>
</body>
</html>
```